Kestrel Photography Business Card

I need a business card designed for a photography business based in Perth, Western Australia called Kestrel Photography.

We specialise in wedding, event photography and portrait photography.

The business card must borrow the style of the attached logo.

The hex codes for the colours in the logo are:
#ED1D85 - Pink
#89C23E - Green
#37282F - Black

The name on the card will be:
Name: Toviran
Phone: 0417395268
Website: www.kestrelphotography.com.au
Facebook: kestrelphotography

I am open and happy to accept creative concepts.

I’d like some space at the back for writing notes and appointment details.

```html
<!DOCTYPE html>
<html lang="en">
<head>
<meta charset="utf-8">
<title>Kestrel Photography – Business Card</title>
<link rel="stylesheet" href="https://fonts.googleapis.com/css2?family=Questrial&family=Montserrat:wght@600&display=swap">
<style>
  :root {
    --pink: #ED1D85;
    --green: #89C23E;
    --ink: #37282F;
    --paper: #FFFFFF;
    --stage: #E9E6E4;
    --wordmark: #4A3D43;
    --contact: #F2EEF0;
  }
  html, body {
    margin: 0;
    padding: 0;
    overflow: hidden;
  }
  .canvas {
    position: relative;
    width: 1200px;
    height: 1000px;
    background: var(--stage);
    overflow: hidden;
    font-family: "Questrial", "Helvetica Neue", Arial, sans-serif;
  }
  .card {
    position: absolute;
    box-shadow: 0 6px 18px rgba(0,0,0,0.18);
    box-sizing: border-box;
  }
  .card--front {
    left: 60px;
    top: 55px;
    width: 740px;
    height: 420px;
    background: var(--paper);
  }
  .card--back {
    left: 342px;
    top: 493px;
    width: 750px;
    height: 434px;
    background: var(--ink);
  }
  .brand-mark {
    position: absolute;
    left: 50%;
    transform: translateX(-50%);
    display: flex;
    align-items: center;
    gap: 22px;
    white-space: nowrap;
    font-family: "Questrial", "Helvetica Neue", Arial, sans-serif;
  }
  .brand-mark__dot {
    flex: none;
    border-radius: 50%;
    background: var(--pink);
  }
  .card--front .brand-mark {
    top: 95px;
    color: var(--ink);
    font-size: 28px;
  }
  .card--front .brand-mark__dot {
    width: 160px;
    height: 160px;
  }
  .card--back .brand-mark {
    top: 48px;
    color: var(--contact);
    font-size: 34px;
  }
  .card--back .brand-mark__dot {
    width: 230px;
    height: 230px;
  }
  .wordmark {
    position: absolute;
    left: 0;
    right: 0;
    bottom: 70px;
    margin: 0;
    padding-left: 0.62em;
    text-align: center;
    font-weight: 400;
    font-size: 25px;
    letter-spacing: 0.62em;
    text-transform: uppercase;
    color: var(--wordmark);
    white-space: nowrap;
  }
  .holder-name {
    position: absolute;
    left: 0;
    right: 0;
    top: 350px;
    margin: 0;
    text-align: center;
    font-family: "Montserrat", Arial, sans-serif;
    font-weight: 600;
    font-size: 21px;
    line-height: 1;
    color: var(--green);
  }
  .contact-line {
    position: absolute;
    left: 0;
    right: 0;
    top: 384px;
    display: flex;
    justify-content: center;
    align-items: center;
    margin: 0;
    padding: 0;
    list-style: none;
    font-size: 17px;
    line-height: 1.3;
    color: var(--contact);
    white-space: nowrap;
  }
  .contact-line li + li {
    border-left: 1px solid var(--pink);
    margin-left: 9px;
    padding-left: 9px;
  }
</style>
</head>
<body>
  <main class="canvas">
    <section class="card card--front" aria-label="Business card front">
      <div class="brand-mark">
        <span class="brand-mark__dot"></span>
        <span class="brand-mark__name">Kestrel Photography</span>
      </div>
      <h1 class="wordmark">Kestrel Photography</h1>
    </section>

    <section class="card card--back" aria-label="Business card back">
      <div class="brand-mark">
        <span class="brand-mark__dot"></span>
        <span class="brand-mark__name">Kestrel Photography</span>
      </div>
      <p class="holder-name">Toviran</p>
      <ul class="contact-line">
        <li class="contact-line__phone">0417395268</li>
        <li class="contact-line__web">www.kestrelphotography.com.au</li>
        <li class="contact-line__social">kestrelphotography</li>
      </ul>
    </section>
  </main>
</body>
</html>
```